Kestrel Electrical Business Card

We need a business card design for our family-run electrical contracting business based in Western Australia called 'Kestrel Electrical'. We provide electrical services including residential, commercial and industrial. We aim for individual business cards to be made for all of our employees. We already have a company logo, which we require to be featured on the design. We would like simple, sleek and vibrant designs, which incorporate our logo and represent our business. We do not want anything involving too many graphics/images. We like the colours red, black, white and all shades of grey. The final design should communicate professionalism and trustworthiness.
We require the following contact information:
Name- Owen Strickland
EC 5809
Mobile number- 0455 918 302
Fax number (including area code)- (08) 9640 2718
Email adress- name@kestrelelectrical.example
Electrical
- ITC Handel Bold

```html
<!DOCTYPE html>
<html lang="en">
<head>
<meta charset="utf-8">
<title>Kestrel Electrical — Business Card</title>
<link rel="stylesheet" href="https://fonts.googleapis.com/css2?family=Exo+2:wght@400;600;700&display=swap">
<style>
  :root {
    --backdrop: #e4e4e6;
    --card-white: #f1f1f2;
    --card-grey: #dcdcde;
    --brand-red: #c1102f;
    --brand-red-deep: #9e0a24;
    --ink-dark: #1d1a24;
    --name-ink: #3b0812;
    --text-light: #ffffff;
  }
  * { box-sizing: border-box; margin: 0; padding: 0; }
  html, body {
    width: 1200px; height: 750px; overflow: hidden;
    background: var(--backdrop);
    font-family: "Exo 2", Arial, sans-serif;
  }
  .canvas {
    position: relative; width: 1200px; height: 750px;
    display: flex; align-items: center; justify-content: center;
  }
  .business-card {
    position: relative; width: 840px; height: 480px;
    border-radius: 40px; overflow: hidden;
    box-shadow: 0 18px 40px rgba(0,0,0,0.18);
  }
  .card-shapes { position: absolute; inset: 0; }
  .brand-lockup {
    position: absolute; left: 48px; top: 214px;
    display: flex; align-items: center; gap: 12px;
    color: var(--ink-dark);
    font-weight: 700; font-size: 26px; letter-spacing: 0.5px;
  }
  .brand-square { width: 22px; height: 22px; background: var(--brand-red); }
  .identity {
    position: absolute; right: 46px; top: 40px; text-align: right;
    color: var(--text-light);
  }
  .identity .person-name {
    font-weight: 700; font-size: 34px; color: var(--name-ink);
    letter-spacing: 0.5px;
  }
  .identity .person-role { font-size: 20px; margin-top: 4px; }
  .identity .licence { font-size: 20px; margin-top: 2px; }
  .contact-line {
    position: absolute; display: flex; align-items: center; gap: 10px;
    color: var(--text-light); font-size: 21px; font-weight: 600;
  }
  .contact-line svg { width: 20px; height: 20px; flex: none; }
  .contact-email { left: 372px; top: 134px; font-weight: 400; }
  .contact-mobile { left: 420px; top: 290px; }
  .contact-fax { left: 420px; top: 324px; }
</style>
</head>
<body>
<main class="canvas">
  <article class="business-card">
    <svg class="card-shapes" viewBox="0 0 840 480" preserveAspectRatio="none" aria-hidden="true">
      <defs>
        <linearGradient id="white-panel" x1="0" y1="0" x2="1" y2="1">
          <stop offset="0" stop-color="var(--card-white)"/>
          <stop offset="1" stop-color="var(--card-grey)"/>
        </linearGradient>
        <linearGradient id="red-panel" x1="0" y1="0" x2="1" y2="1">
          <stop offset="0" stop-color="var(--brand-red)"/>
          <stop offset="1" stop-color="var(--brand-red-deep)"/>
        </linearGradient>
      </defs>
      <rect width="840" height="480" fill="url(#red-panel)"/>
      <path d="M0 0 H300 C370 120 370 330 270 480 H0 Z" fill="var(--ink-dark)"/>
      <path d="M0 0 H286 C350 120 345 320 240 480 H0 Z" fill="url(#white-panel)"/>
    </svg>

    <div class="brand-lockup">
      <span class="brand-square"></span>
      <span class="brand-name">Kestrel Electrical</span>
    </div>

    <div class="identity">
      <p class="person-name">Owen Strickland</p>
      <p class="person-role">director</p>
      <p class="licence">EC 5809</p>
    </div>

    <p class="contact-line contact-email">
      <svg viewBox="0 0 20 20"><circle cx="10" cy="10" r="10" fill="var(--ink-dark)"/><rect x="5" y="6.5" width="10" height="7" fill="none" stroke="#fff" stroke-width="1.3"/><path d="M5 6.5 L10 10.5 L15 6.5" fill="none" stroke="#fff" stroke-width="1.3"/></svg>
      name@kestrelelectrical.example
    </p>
    <p class="contact-line contact-mobile">
      <svg viewBox="0 0 20 20"><path d="M5 2 L8 2 L9 6 L7 8 C8 10.5 9.5 12 12 13 L14 11 L18 12 L18 15 C18 16.5 16.5 18 15 18 C8 17.5 2.5 12 2 5 C2 3.5 3.5 2 5 2 Z" fill="#fff"/></svg>
      0455 918 302
    </p>
    <p class="contact-line contact-fax">
      <svg viewBox="0 0 20 20"><rect x="5" y="2" width="10" height="6" fill="#fff"/><rect x="2" y="8" width="16" height="8" rx="1.5" fill="#fff"/><rect x="5" y="13" width="10" height="5" fill="#fff" stroke="var(--brand-red)" stroke-width="1"/></svg>
      (08) 9640 2718
    </p>
  </article>
</main>
</body>
</html>
```